Business Cards and Letterhead
for Modern Boston Law Firm
Simple
Gerald Dunmore
71 Ashworth Street
5th Floor
Boston, Massachusetts 02108
ger@dunmorekp-example.com
www.dunmorekp-example.com

```html
<!DOCTYPE html>
<html lang="en">
<head>
<meta charset="UTF-8">
<title>Dunmore Law Group – Business Card</title>
<link rel="stylesheet" href="https://fonts.googleapis.com/css2?family=Cinzel:wght@400;600&display=swap">
<style>
  :root {
    --backdrop: #ece9e4;
    --card-red: #b21f2b;
    --card-red-dark: #8e1620;
    --paper: #ffffff;
    --ink-grey: #6d6d6d;
    --rule-grey: #c9c9c9;
  }
  * { margin: 0; padding: 0; box-sizing: border-box; }
  html, body {
    width: 1200px; height: 914px; overflow: hidden;
    background: var(--backdrop);
    font-family: "Cinzel", "Times New Roman", serif;
  }
  .business-card {
    position: absolute; left: 100px; top: 167px;
    width: 1000px; height: 580px;
    background: linear-gradient(135deg, var(--card-red), var(--card-red-dark));
    padding: 30px;
    box-shadow: 0 10px 30px rgba(0,0,0,0.18);
  }
  .card-face {
    position: relative; width: 100%; height: 100%;
    background: var(--paper);
  }
  .firm-mark {
    position: absolute; left: 250px; top: 120px;
    display: flex; align-items: center; gap: 22px;
  }
  .firm-mark__dot {
    width: 74px; height: 74px; border-radius: 50%;
    background: var(--ink-grey);
  }
  .firm-mark__name {
    font-size: 40px; font-weight: 600; color: var(--card-red);
    letter-spacing: 1px;
  }
  .contact-block {
    position: absolute; left: 0; top: 262px; width: 100%;
  }
  .person {
    position: absolute; right: 530px; top: 0;
    text-align: right; color: var(--ink-grey);
    font-size: 17px; line-height: 30px; letter-spacing: 0.5px;
  }
  .person__name {
    color: var(--card-red); font-size: 22px; margin-bottom: 6px;
  }
  .divider {
    position: absolute; left: 480px; top: 4px;
    width: 1px; height: 168px; background: var(--rule-grey);
  }
  .reach {
    position: absolute; left: 500px; top: 36px;
    list-style: none; color: var(--ink-grey);
    font-size: 17px; letter-spacing: 0.5px;
  }
  .reach__item {
    display: flex; align-items: center; gap: 12px; height: 30px;
  }
  .reach__icon { width: 20px; height: 20px; flex: none; }
</style>
</head>
<body>
  <div class="business-card">
    <div class="card-face">
      <div class="firm-mark">
        <span class="firm-mark__dot"></span>
        <span class="firm-mark__name">Dunmore Law Group, LLC</span>
      </div>

      <div class="contact-block">
        <div class="person">
          <p class="person__name">Gerald Dunmore</p>
          <p>71 Ashworth Street, 5th Floor</p>
          <p>Boston,</p>
          <p>Massachusetts 02108</p>
        </div>

        <span class="divider"></span>

        <ul class="reach">
          <li class="reach__item">
            <svg class="reach__icon" viewBox="0 0 20 20"><circle cx="10" cy="10" r="10" fill="#b21f2b"/><path d="M6.5 5.5l2 0 1 2.5-1.2 1a6 6 0 0 0 2.7 2.7l1-1.2 2.5 1v2c0 .6-.5 1-1 1A8.5 8.5 0 0 1 5.5 6.5c0-.5.4-1 1-1z" fill="#fff"/></svg>
            <span>617-555-0142</span>
          </li>
          <li class="reach__item">
            <svg class="reach__icon" viewBox="0 0 20 20"><circle cx="10" cy="10" r="10" fill="#b21f2b"/><rect x="7" y="4.5" width="6" height="11" rx="1" fill="#fff"/><rect x="8" y="6" width="4" height="7" fill="#b21f2b"/></svg>
            <span>617-555-0187</span>
          </li>
          <li class="reach__item">
            <svg class="reach__icon" viewBox="0 0 20 20"><circle cx="10" cy="10" r="10" fill="#b21f2b"/><rect x="5" y="6.5" width="10" height="7" fill="#fff"/><path d="M5 6.5l5 4 5-4" fill="none" stroke="#b21f2b" stroke-width="1"/></svg>
            <span>ger@dunmorekp-example.com</span>
          </li>
          <li class="reach__item">
            <svg class="reach__icon" viewBox="0 0 20 20"><circle cx="10" cy="10" r="10" fill="#b21f2b"/><circle cx="10" cy="10" r="5" fill="none" stroke="#fff" stroke-width="1.2"/><ellipse cx="10" cy="10" rx="2.2" ry="5" fill="none" stroke="#fff" stroke-width="1"/><line x1="5" y1="10" x2="15" y2="10" stroke="#fff" stroke-width="1"/></svg>
            <span>www.dunmorekp-example.com</span>
          </li>
        </ul>
      </div>
    </div>
  </div>
</body>
</html>
```